Home care support

Design a a great and dynamic website for a healthcare business. Our business will be involved in providing care at home for people with disability and the elderly. Below is a link that I found for a company offering similar services in the US. I am looking for something like this .
I have my files - the latest project in here in through through PixelNest
Sample site : https://pinegroveattendants.net/
Target Market(s)
people with disability and elderly seniors who need home care support
Industry/Entity Type
Health
Coding
Coded - Design and coding required
Number of Pages Required
5+ page
Requirements
Must have
- inspirational pictures and designed with the themed logo (files attached)
Nice to have
- This is my sample and should look like this : https://pinegroveattendants.net/

```html
<!DOCTYPE html>
<html lang="en">
<head>
<meta charset="utf-8">
<title>Hollowbrook Homecare</title>
<link href="https://fonts.googleapis.com/css2?family=Libre+Baskerville:wght@400;700&family=Lato:wght@400;700&family=Poppins:wght@400&display=swap" rel="stylesheet">
<style>
:root{
  --blue:#1a8fd6;
  --blue-deep:#1a6fb5;
  --blue-pale:#bfe3f6;
  --ink:#2a2a2a;
  --body:#4a4a4a;
  --grey-band:#eef0f2;
  --footer:#1a7fcb;
  --white:#ffffff;
}
*{margin:0;padding:0;box-sizing:border-box}
html,body{width:1200px;height:4225px;overflow:hidden;background:var(--white)}
body{position:relative;font-family:"Lato",sans-serif;color:var(--body)}
.abs{position:absolute}
.serif{font-family:"Libre Baskerville",serif;font-weight:700;letter-spacing:1px}
.hl{color:var(--blue-deep)}
.btn{position:absolute;background:var(--blue);color:var(--white);font:700 17px "Lato",sans-serif;display:flex;align-items:center;justify-content:center;gap:10px;text-transform:uppercase;letter-spacing:.3px}
.btn svg{width:15px;height:15px}
.para{font-size:16px;line-height:31.5px;color:var(--body)}

/* header */
.topline{left:0;top:0;width:1200px;height:6px;background:var(--blue)}
.phone-tab{left:828px;top:0;width:372px;height:49px;background:var(--blue);border-bottom-left-radius:26px;color:var(--white);display:flex;align-items:center;gap:14px;padding-left:36px;font:700 24px "Libre Baskerville",serif;letter-spacing:1px}
.brand{left:75px;top:36px;display:flex;align-items:center;gap:10px}
.brand-dot{width:26px;height:26px;border-radius:50%;background:var(--blue-deep)}
.brand-name{font:700 20px "Libre Baskerville",serif;color:var(--blue-deep);line-height:1.15}
.nav{top:92px;font:700 13.5px "Lato",sans-serif;color:var(--ink);text-transform:uppercase}
.nav.active{color:var(--blue)}

/* hero */
.hero-photo{left:0;top:143px;width:1200px;height:598px;background:linear-gradient(90deg,#7d7873 0%,#b4aca4 40%,#d8cfc6 70%,#9c8c82 100%)}
.hero-title{left:75px;top:296px;font-size:62px;line-height:60px;color:var(--white)}
.hero-sub{left:76px;top:420px;font:400 29px/41px "Poppins",sans-serif;color:var(--white)}
.dots{left:551px;top:686px;display:flex;gap:15px}
.dots span{width:15px;height:15px;border-radius:50%;background:var(--white)}
.dots span:first-child{background:var(--blue)}

/* circle photos */
.ring{position:absolute;border-radius:50%;background:var(--blue-pale)}
.photo{position:absolute;border-radius:50%;border:6px solid var(--white)}

/* services */
.services-band{left:0;top:1356px;width:1200px;height:759px;background:var(--grey-band)}
.h2{font-size:33px;color:var(--ink)}
.svc-title{font-size:19px;color:var(--blue-deep);letter-spacing:1px}
.svc-text{font-size:14.5px;line-height:25px;color:var(--body)}

/* why */
.why-band{left:0;top:2719px;width:1200px;height:508px;background:linear-gradient(100deg,#1a7fcb 0%,#2b95d9 60%,#5cc1ea 100%)}
.card{position:absolute;top:2865px;width:241px;height:292px;background:var(--white);text-align:center;box-shadow:0 12px 16px -8px rgba(0,0,0,.35)}
.card svg{margin-top:26px;width:94px;height:94px}
.card h3{font:700 16px "Libre Baskerville",serif;color:var(--ink);letter-spacing:1px;margin-top:10px;line-height:23px}
.card p{font-size:13.5px;line-height:24px;color:var(--body);margin:10px 20px 0}

/* form */
.field{position:absolute;left:617px;width:436px;border:1.5px solid #c8c8c8;font:700 13.5px "Lato",sans-serif;color:var(--ink);padding:14px 16px}

/* footer */
.footer{left:0;top:3864px;width:1200px;height:361px;background:var(--footer);color:var(--white)}
.f-head{font:700 18px "Lato",sans-serif;color:var(--white)}
.f-list{font-size:14.5px;line-height:29.5px;color:#dcefff;list-style:none}
.social{display:flex;gap:16px}
.social span{width:22px;height:22px;border-radius:50%;background:var(--white)}
</style>
</head>
<body>

<!-- header -->
<div class="abs topline"></div>
<div class="abs phone-tab">
  <svg width="22" height="22" viewBox="0 0 24 24"><path fill="#fff" d="M6.6 10.8a15 15 0 0 0 6.6 6.6l2.2-2.2c.3-.3.7-.4 1-.2 1.1.4 2.3.6 3.6.6.6 0 1 .4 1 1V20c0 .6-.4 1-1 1A17 17 0 0 1 3 4c0-.6.4-1 1-1h3.5c.6 0 1 .4 1 1 0 1.3.2 2.5.6 3.6.1.3 0 .7-.2 1z"/></svg>
  +1-800-555-0148
</div>
<div class="abs brand">
  <span class="brand-dot"></span>
  <span class="brand-name">HOLLOWBROOK<br>HOMECARE</span>
</div>
<div class="abs nav active" style="left:394px">Home</div>
<div class="abs nav" style="left:500px">About Us</div>
<div class="abs nav" style="left:636px">Services</div>
<div class="abs nav" style="left:764px">Resources</div>
<div class="abs nav" style="left:910px">Careers</div>
<div class="abs nav" style="left:1036px">Contact Us</div>

<!-- hero -->
<div class="abs hero-photo" role="img" aria-label="Young carer gently holding an elderly smiling woman seated at home"></div>
<div class="abs serif hero-title">HOLLOWBROOK<br>HOMECARE</div>
<div class="abs hero-sub">We care at home for people with<br>disability and the elderly.</div>
<div class="btn" style="left:75px;top:523px;width:182px;height:56px">Read More <svg viewBox="0 0 16 16"><circle cx="8" cy="8" r="8" fill="#fff"/><path d="M6 4.5 9.5 8 6 11.5" stroke="#1a8fd6" stroke-width="2" fill="none"/></svg></div>
<div class="abs dots"><span></span><span></span><span></span><span></span></div>

<!-- welcome -->
<div class="ring" style="left:85px;top:830px;width:466px;height:466px"></div>
<div class="photo" role="img" aria-label="Male nurse kneeling beside a senior man with a walking frame" style="left:82px;top:808px;width:462px;height:462px;background:linear-gradient(135deg,#e8e4df,#a9a39c 55%,#7d2a33)"></div>
<div class="abs serif" style="left:587px;top:866px;font-size:32px;line-height:39px;color:var(--ink)">WELCOME TO<br><span class="hl">HOLLOWBROOK HOMECARE</span></div>
<p class="abs para" style="left:587px;top:955px;width:540px">Sed ut perspiciatis unde omnis iste natus error sit voluptatem accusantium doloremque laudantium, totam rem aperiam, eaque ipsa quae ab illo inventore veritatis et quasi architecto beatae vitae dicta sunt explicabo. Nemo enim ipsam voluptatem quia voluptas sit aspernatur aut odit aut fugit, sed quia consequuntur magni dolores eos qui ratione voluptatem sequi nesciunt.</p>
<div class="btn" style="left:587px;top:1171px;width:181px;height:54px">Read More <svg viewBox="0 0 16 16"><circle cx="8" cy="8" r="8" fill="#fff"/><path d="M6 4.5 9.5 8 6 11.5" stroke="#1a8fd6" stroke-width="2" fill="none"/></svg></div>

<!-- services -->
<div class="abs services-band"></div>
<div class="abs serif h2" style="left:0;width:1200px;top:1428px;text-align:center">OUR <span class="hl">SERVICES</span></div>

<div class="abs serif svc-title" style="left:0;width:1200px;top:1512px;text-align:center">MEAL PREPARATION</div>
<p class="abs svc-text" style="left:455px;width:294px;top:1544px;text-align:center">Sed ut perspiciatis unde omnis iste natus error sit voluptatem accusantium doloremque</p>

<div class="abs serif svc-title" style="left:60px;width:301px;top:1711px;text-align:right">COMPANION CARE</div>
<p class="abs svc-text" style="left:75px;width:286px;top:1744px;text-align:right">Sed ut perspiciatis unde omnis iste natus error sit voluptatem accusantium doloremque</p>

<div class="abs serif svc-title" style="left:856px;top:1711px">AMBULATION ASSISTANCE</div>
<p class="abs svc-text" style="left:856px;width:280px;top:1744px">Sed ut perspiciatis unde omnis iste nat error sit voluptatem accusantium doloremque</p>

<div class="abs serif svc-title" style="left:40px;width:260px;top:1873px;text-align:right">TRANSPORTATION</div>
<p class="abs svc-text" style="left:85px;width:215px;top:1907px;text-align:right">Sed ut perspiciatis unde omnis iste natus error sit voluptatem accusantium doloremque</p>

<div class="abs serif svc-title" style="left:907px;top:1873px;line-height:25px">KITCHEN &amp;<br>BATHROOM</div>
<p class="abs svc-text" style="left:907px;width:220px;top:1932px">Sed ut perspiciatis unde omnis iste natus error sit voluptatem accusantium doloremque</p>

<svg class="abs" style="left:0;top:1356px" width="1200" height="759" viewBox="0 1356 1200 759">
  <g fill="none" stroke="#8a8f95" stroke-width="3">
    <path d="M472 1927 A130 130 0 0 1 732 1927"/>
    <line x1="602" y1="1797" x2="602" y2="1772"/>
    <line x1="510" y1="1835" x2="492" y2="1817"/>
    <line x1="694" y1="1835" x2="712" y2="1817"/>
    <line x1="472" y1="1927" x2="448" y2="1923"/>
    <line x1="732" y1="1927" x2="756" y2="1923"/>
  </g>
  <g fill="#fff" stroke="#8a8f95" stroke-width="3">
    <circle cx="602" cy="1797" r="7"/><circle cx="510" cy="1835" r="7"/><circle cx="694" cy="1835" r="7"/>
    <circle cx="472" cy="1927" r="7"/><circle cx="732" cy="1927" r="7"/>
  </g>
  <g fill="none" stroke="#9aa0a6" stroke-width="1.5" stroke-dasharray="5 5">
    <circle cx="602" cy="1705" r="66"/><circle cx="448" cy="1771" r="66"/><circle cx="757" cy="1771" r="66"/>
    <circle cx="382" cy="1919" r="66"/><circle cx="820" cy="1919" r="66"/>
  </g>
  <g fill="#1a8fd6">
    <circle cx="602" cy="1705" r="54"/><circle cx="448" cy="1771" r="54"/><circle cx="757" cy="1771" r="54"/>
    <circle cx="382" cy="1919" r="54"/><circle cx="820" cy="1919" r="54"/>
  </g>
  <g fill="none" stroke="#fff" stroke-width="3" stroke-linecap="round">
    <circle cx="602" cy="1705" r="20"/><circle cx="602" cy="1705" r="12"/>
    <line x1="572" y1="1688" x2="572" y2="1725"/><line x1="632" y1="1688" x2="632" y2="1725"/>
    <circle cx="436" cy="1752" r="7"/><path d="M424 1796v-22a12 12 0 0 1 24 0v22"/>
    <circle cx="462" cy="1756" r="6"/><path d="M452 1796v-18a10 10 0 0 1 20 0v18"/>
    <rect x="730" y="1757" width="40" height="26" rx="3"/><path d="M770 1765h10l6 9v9h-16"/>
    <circle cx="744" cy="1786" r="5"/><circle cx="778" cy="1786" r="5"/>
    <line x1="750" y1="1762" x2="750" y2="1776"/><line x1="743" y1="1769" x2="757" y2="1769"/>
    <rect x="355" y="1902" width="54" height="28" rx="5"/><line x1="355" y1="1914" x2="409" y2="1914"/>
    <circle cx="367" cy="1933" r="5"/><circle cx="397" cy="1933" r="5"/>
    <rect x="796" y="1905" width="48" height="36" rx="2"/><line x1="796" y1="1920" x2="844" y2="1920"/>
    <rect x="804" y="1926" width="14" height="10"/><rect x="826" y="1894" width="16" height="11"/>
  </g>
  <circle cx="602" cy="1927" r="98" fill="#fff" stroke="#1a6fb5" stroke-width="2"/>
  <circle cx="602" cy="1927" r="86" fill="none" stroke="#bfe3f6" stroke-width="2"/>
  <text x="602" y="1921" text-anchor="middle" font-family="Libre Baskerville, serif" font-weight="700" font-size="17" fill="#1a6fb5" letter-spacing="1">HOLLOWBROOK</text>
  <text x="602" y="1945" text-anchor="middle" font-family="Libre Baskerville, serif" font-weight="700" font-size="17" fill="#1a6fb5" letter-spacing="1">HOMECARE</text>
</svg>

<!-- approach -->
<div class="abs serif" style="left:75px;top:2227px;font-size:32px;line-height:40px;color:var(--ink)"><span class="hl">A SIMPLE,</span> AFFORDABLE<br>APPROACH TO <span class="hl">HOME CARE</span></div>
<p class="abs para" style="left:75px;top:2317px;width:540px">Sed ut perspiciatis unde omnis iste natus error sit voluptatem accusantium doloremque laudantium, totam rem aperiam, eaque ipsa quae ab illo inventore veritatis et quasi architecto beatae vitae dicta sunt explicabo. Nemo enim ipsam voluptatem quia voluptas sit aspernatur aut odit aut fugit, sed quia consequuntur magni dolores eos qui ratione voluptatem sequi nesciunt.</p>
<div class="btn" style="left:75px;top:2534px;width:182px;height:54px">Read More <svg viewBox="0 0 16 16"><circle cx="8" cy="8" r="8" fill="#fff"/><path d="M6 4.5 9.5 8 6 11.5" stroke="#1a8fd6" stroke-width="2" fill="none"/></svg></div>
<div class="ring" style="left:658px;top:2178px;width:466px;height:466px"></div>
<div class="photo" role="img" aria-label="Senior woman with a cane seated on a sofa, a carer resting a hand on her shoulder" style="left:672px;top:2172px;width:448px;height:448px;background:linear-gradient(135deg,#c9d3d0,#8b9a98 45%,#a5825f)"></div>

<!-- why choose us -->
<div class="abs why-band"></div>
<div class="abs serif" style="left:0;width:1200px;top:2779px;text-align:center;font-size:32px;color:var(--white)">WHY CHOOSE US</div>

<div class="card" style="left:75px">
  <svg viewBox="0 0 94 94" fill="none" stroke="#1a6fb5" stroke-width="2.5"><circle cx="40" cy="28" r="14"/><path d="M14 82v-10a26 26 0 0 1 52 0v10z"/><circle cx="66" cy="68" r="13" fill="#fff"/><text x="66" y="73" text-anchor="middle" font-size="13" font-family="Lato,sans-serif" fill="#1a6fb5" stroke="none" font-weight="700">24</text></svg>
  <h3>ON CALL 24/7</h3>
  <p>Sed ut perspiciatis unde omnis iste natus error sit voluptatem accusantium architecto beatae vitae dicta .</p>
</div>
<div class="card" style="left:346px">
  <svg viewBox="0 0 94 94" fill="none" stroke="#1a6fb5" stroke-width="2.5"><circle cx="47" cy="50" r="22"/><path d="M47 14v10M25 22l6 7M69 22l-6 7M14 44h9M71 44h9M38 58q9 6 18 0"/></svg>
  <h3>PEACE OF MIND</h3>
  <p>Sed ut perspiciatis unde omnis iste natus error sit voluptatem accusantium architecto beatae vitae dicta .</p>
</div>
<div class="card" style="left:615px">
  <svg viewBox="0 0 94 94" fill="none" stroke="#1a6fb5" stroke-width="2.5"><rect x="12" y="18" width="62" height="58" rx="4"/><line x1="12" y1="32" x2="74" y2="32"/><path d="M26 12v12M60 12v12"/><rect x="22" y="40" width="9" height="8"/><rect x="38" y="40" width="9" height="8"/><rect x="22" y="56" width="9" height="8"/><circle cx="68" cy="70" r="13" fill="#fff"/><path d="M62 70l5 5 8-9"/></svg>
  <h3>FLEXIBLE SCHEDULE</h3>
  <p>Sed ut perspiciatis unde omnis iste natus error sit voluptatem accusantium architecto beatae vitae dicta .</p>
</div>
<div class="card" style="left:886px">
  <svg viewBox="0 0 94 94" fill="none" stroke="#1a6fb5" stroke-width="2.5"><circle cx="47" cy="24" r="9"/><path d="M33 50a14 14 0 0 1 28 0"/><path d="M12 40l12 30 16 8M82 40l-12 30-16 8"/></svg>
  <h3>CHOICE<br>OF CAREGIVER</h3>
  <p>Sed ut perspiciatis unde omnis iste natus error sit voluptatem accusantium architecto.</p>
</div>

<!-- contact -->
<div class="ring" style="left:85px;top:3308px;width:466px;height:466px"></div>
<div class="photo" role="img" aria-label="Carer in scrubs showing a tablet to a smiling senior woman" style="left:82px;top:3286px;width:462px;height:462px;background:linear-gradient(135deg,#e7e0d6,#7b5a45 50%,#2f5fa8)"></div>
<div class="abs serif" style="left:615px;top:3320px;font-size:32px;line-height:39px;color:var(--ink)">THE BEST HOME CARE<br>STARTS HERE</div>
<div class="abs serif" style="left:615px;top:3416px;font-size:16.5px;font-weight:400;color:var(--blue-deep);letter-spacing:1px">FLEXIBLE APPOINTMENTS AND CARE OPTIONS.</div>
<div class="field" style="top:3465px;height:46px">NAME</div>
<div class="field" style="top:3526px;height:46px">EMAIL ADDRESS</div>
<div class="field" style="top:3587px;height:102px">MESSAGE</div>
<div class="btn" style="left:617px;top:3721px;width:180px;height:54px">Submit <svg viewBox="0 0 16 16"><circle cx="8" cy="8" r="8" fill="#fff"/><path d="M6 4.5 9.5 8 6 11.5" stroke="#1a8fd6" stroke-width="2" fill="none"/></svg></div>

<!-- footer -->
<div class="abs footer"></div>
<div class="abs" style="left:75px;top:3950px;display:flex;align-items:center;gap:12px">
  <span style="width:34px;height:34px;border-radius:50%;background:#fff"></span>
  <span style="font:700 25px/30px 'Libre Baskerville',serif;color:#fff">HOLLOWBROOK<br>HOMECARE</span>
</div>
<div class="abs" style="left:75px;top:4088px;font-size:13.5px;line-height:24px;color:#fff">Copyright &copy; 2022 Hollowbrook Homecare.<br>All Rights Reserved.</div>

<div class="abs f-head" style="left:369px;top:3922px">SITE MAP</div>
<ul class="abs f-list" style="left:369px;top:3951px"><li>Home</li><li>About Us</li><li>Services</li><li>Resources</li><li>Careers</li><li>Contact Us</li></ul>

<div class="abs f-head" style="left:605px;top:3922px">RESOURCES</div>
<ul class="abs f-list" style="left:605px;top:3951px"><li>Sed ut perspiciatis</li><li>Unde omnis iste natus</li><li>Error sit voluptatem</li><li>Accusantium</li><li>Doloremque</li></ul>

<div class="abs f-head" style="left:884px;top:3922px">OUR LOCATIONS</div>
<div class="abs" style="left:884px;top:3955px;font:700 14px 'Lato',sans-serif;color:#fff">HOLLOWBROOK HOMECARE</div>
<div class="abs" style="left:884px;top:3982px;font-size:14.5px;line-height:26px;color:#dcefff">12 Alder Row, Fenwick,<br>Marlow, UK</div>
<div class="abs" style="left:884px;top:4045px;display:flex;gap:16px;align-items:center;font-size:14.5px;color:#dcefff">
  <svg width="14" height="14" viewBox="0 0 24 24"><path fill="#fff" d="M6.6 10.8a15 15 0 0 0 6.6 6.6l2.2-2.2c.3-.3.7-.4 1-.2 1.1.4 2.3.6 3.6.6.6 0 1 .4 1 1V20c0 .6-.4 1-1 1A17 17 0 0 1 3 4c0-.6.4-1 1-1h3.5c.6 0 1 .4 1 1 0 1.3.2 2.5.6 3.6.1.3 0 .7-.2 1z"/></svg>+1-800-555-0148</div>
<div class="abs" style="left:884px;top:4080px;display:flex;gap:16px;align-items:center;font-size:14.5px;color:#dcefff">
  <svg width="14" height="12" viewBox="0 0 24 20"><rect width="24" height="20" rx="2" fill="#fff"/><path d="M1 2l11 9 11-9" stroke="#1a7fcb" stroke-width="2" fill="none"/></svg>hello@hollowbrookcare.com</div>
<div class="abs social" style="left:884px;top:4130px"><span></span><span></span><span></span><span></span><span></span></div>

</body>
</html>
```